Corvella Web Design Project

I am attaching my logo so I need to see applied to the website developed by you guys!!
Tbahks!!
Ferruccio
This is the DNA of the company
Flat and dynamic organization - Informal and respectful social approac
Innovative - Always striving for the best solution
Reliability and Quality - The value of our name
Flexibility - Ability to handle new requirements and unforeseen events
Simplicity - Technology must serve – NOT rule!
Cooperative Relations - The synergy that makes 1+1=3
We still don´t have our logo as we have another open project on artbazaarly
Our company won´t be selling this equipment but providing welding services for shipyard industry, as you can see on the website below.
www.velmorasystems.example
Reason: Hi webdesigners,
I will be deciding my logo by this weekend as soon as I have decided I will post my logo to see it applied to your design!!!
Thanks
Ferruccio
I just Sent my logo for your attention!!!!
Welding

```html
<!DOCTYPE html>
<html lang="en">
<head>
<meta charset="utf-8">
<title>Corvella – Welding Services</title>
<link href="https://fonts.googleapis.com/css2?family=Roboto:wght@300;400;500;700&family=Open+Sans:wght@400;600&display=swap" rel="stylesheet">
<style>
:root{
  --ink:#0f0b08;
  --header:#120c07;
  --orange:#f0a52a;
  --orange-deep:#e08f14;
  --accent-text:#e59a1e;
  --text:#3b3b3b;
  --muted:#777;
  --line:#e6e6e6;
  --footer:#050505;
  --footer-bottom:#1c1c1c;
  --white:#fff;
}
*{box-sizing:border-box;margin:0;padding:0}
html,body{width:797px;height:1200px;overflow:hidden;background:var(--white)}
body{position:relative;font-family:"Roboto",sans-serif;color:var(--text)}
.abs{position:absolute}

/* header */
.site-header{left:0;top:0;width:797px;height:114px;background:var(--header)}
.brand{left:116px;top:38px;display:flex;align-items:center;gap:8px}
.brand-mark{width:22px;height:22px;background:var(--white)}
.brand-name{font-family:"Roboto",sans-serif;font-weight:700;font-size:31px;color:var(--orange);letter-spacing:-.5px}
.search{left:570px;top:18px;width:114px;height:21px;background:var(--white);border:1px solid #ccc;font-family:"Open Sans",sans-serif;font-size:7px;color:#999;padding:5px 8px}
.search svg{position:absolute;right:8px;top:6px}
.downloads{left:621px;top:58px;width:63px;height:21px;background:var(--orange);border:1px solid #c77e0c;font-size:8px;color:#2a1a05;display:flex;align-items:center;justify-content:center}

/* nav */
.main-nav{left:114px;top:97px;width:570px;height:34px;background:linear-gradient(#f5b03b,var(--orange));display:flex;box-shadow:0 6px 8px -4px rgba(0,0,0,.25)}
.main-nav a{color:var(--white);text-decoration:none;font-size:10.5px;display:flex;align-items:center;justify-content:center;border-right:1px solid rgba(0,0,0,.12)}
.main-nav a:last-child{border-right:0}

/* hero */
.hero{left:114px;top:149px;width:570px;height:301px;background:linear-gradient(100deg,#3c5e86 0%,#56789a 30%,#7a6650 55%,#d98a22 72%,#3a3530 100%);box-shadow:0 8px 10px -6px rgba(0,0,0,.35)}
.hero-words{left:452px;top:248px;font-family:"Open Sans",sans-serif;font-weight:600;font-size:31px;line-height:42px;color:var(--white);text-shadow:1px 2px 3px rgba(0,0,0,.5)}
.hero-arrow{top:376px;width:18px;height:18px;display:flex;align-items:center;justify-content:center}
.hero-arrow.prev{left:456px;background:#e2661b}
.hero-arrow.next{left:475px;background:#2a2520}

/* welcome */
.welcome-title{left:0;width:797px;top:466px;text-align:center;font-size:22px;color:#333}
.welcome-title span{color:var(--accent-text)}
.welcome-text{left:114px;width:570px;top:501px;text-align:center;font-family:"Open Sans",sans-serif;font-size:7.4px;line-height:13.6px;color:#666}

/* cards */
.card{top:561px;width:177px;height:201px;background:#fafafa;box-shadow:0 2px 3px rgba(0,0,0,.12)}
.card-photo{height:98px;border-bottom:2px solid var(--orange)}
.card h3{font-weight:400;font-size:12px;color:#333;text-align:center;margin-top:12px}
.card p{font-family:"Open Sans",sans-serif;font-size:6.8px;line-height:13.6px;color:#777;text-align:center;padding:0 14px;margin-top:7px}
.card .more{display:block;text-align:center;font-family:"Open Sans",sans-serif;font-size:7px;color:#333;margin-top:5px}

/* video */
.video{left:114px;top:798px;width:288px;height:138px;background:radial-gradient(circle at 78% 85%,#fff5d8 0%,#e2a63a 18%,#6a4a22 40%,#151820 70%)}
.play{left:237px;top:847px}
.video-bar{left:114px;top:936px;width:288px;height:18px;background:#f1f1f1;border:1px solid #ddd;font-size:4.5px;color:#444}

/* recent work */
.recent-title{left:425px;top:795px;font-size:13.5px;color:#333}
.recent-rule{left:425px;top:824px;width:259px;height:1px;background:var(--line)}
.recent-photo{left:424px;top:839px;width:116px;height:116px;background:linear-gradient(#7b8fa0 0%,#8d9aa2 30%,#c94a2a 55%,#d8452c 75%,#4a5566 100%)}
.recent-heading{left:552px;top:838px;font-size:9.6px;color:#333}
.recent-text{left:550px;top:855px;width:134px;font-family:"Open Sans",sans-serif;font-size:7px;line-height:13.1px;color:#777}
.read-more{left:551px;top:942px;display:flex;align-items:center;gap:6px;font-family:"Open Sans",sans-serif;font-size:7.2px;color:#222;text-decoration:underline}

/* footer */
.site-footer{left:0;top:990px;width:797px;height:170px;background:var(--footer)}
.fb-logo{left:117px;top:1012px;width:77px;height:34px;border:1px solid #333;background:#000;display:flex;align-items:center;justify-content:center;gap:4px}
.fb-logo .brand-name{font-size:13px;color:var(--white)}
.fb-logo .brand-mark{width:9px;height:9px}
.fb-count{left:201px;top:1012px;font-size:7.5px;color:#888}
.fb-like{left:201px;top:1029px;width:28px;height:10px;background:#3b5998}
.fb-grid{left:117px;top:1052px;display:grid;grid-template-columns:repeat(5,28px);gap:2px}
.fb-grid div{height:28px;background:linear-gradient(#6b7b6a,#a89a86)}
.fb-rule{left:117px;top:1125px;width:150px;height:1px;background:#333}
.fb-plugin{left:120px;top:1130px;font-size:7.8px;color:#bbb;display:flex;align-items:center;gap:9px}
.fb-plugin i{width:6px;height:6px;background:#4a66a0;display:block}
.footer-heading{font-size:12px;color:#ddd;font-weight:300;letter-spacing:.3px}
.news-title{left:331px;top:1010px}
.news-text{left:331px;top:1030px;width:190px;font-family:"Open Sans",sans-serif;font-size:6.6px;line-height:12.8px;color:#ccc}
.news-input{left:331px;top:1068px;width:125px;height:29px;background:#0b0b0b;border:1px solid #222;font-family:"Open Sans",sans-serif;font-size:6.8px;color:#888;padding:10px 7px}
.news-btn{left:456px;top:1068px;width:50px;height:29px;background:var(--orange);font-size:10.5px;color:#2a1a05;display:flex;align-items:center;justify-content:center}
.social{top:1109px;display:flex;flex-direction:column;align-items:center;gap:2px;font-family:"Open Sans",sans-serif;font-size:5.5px;color:#bbb}
.social span{width:23px;height:23px;border:1.5px solid #ddd;border-radius:50%;display:block}
.address-title{left:579px;top:1003px}
.address-text{left:580px;top:1026px;font-family:"Open Sans",sans-serif;font-size:7.3px;line-height:13.6px;color:#ccc}
.phone-title{left:581px;top:1065px}
.phone-text{left:581px;top:1090px;font-size:8.5px;color:#ddd;line-height:23px}
.footer-bottom{left:0;top:1160px;width:797px;height:40px;background:var(--footer-bottom)}
.copyright{left:331px;top:1176px;font-size:7.8px;color:#ccc}
</style>
</head>
<body>

<header class="abs site-header"></header>
<div class="abs brand"><span class="brand-mark"></span><span class="brand-name">Corvella</span></div>
<div class="abs search">Search
  <svg width="8" height="8" viewBox="0 0 8 8"><circle cx="3.3" cy="3.3" r="2.5" fill="none" stroke="#999" stroke-width="1"/><line x1="5.2" y1="5.2" x2="7.5" y2="7.5" stroke="#999" stroke-width="1"/></svg>
</div>
<div class="abs downloads">DOWNLOADS</div>

<nav class="abs main-nav">
  <a style="width:70px">Home</a>
  <a style="width:80px">About Us</a>
  <a style="width:94px">Competence</a>
  <a style="width:86px">Case Story</a>
  <a style="width:80px">Products</a>
  <a style="width:69px">Videos</a>
  <a style="width:91px">Contact Us</a>
</nav>

<div class="abs hero" role="img" aria-label="Orange industrial welding robot arm throwing sparks in a workshop"></div>
<div class="abs hero-words">INNOVATIVE<br>RELIABLE<br>FLEXIBLE</div>
<div class="abs hero-arrow prev"><svg width="6" height="7" viewBox="0 0 6 7"><path d="M4 1 L1.5 3.5 L4 6" fill="none" stroke="#fff" stroke-width="1.2"/></svg></div>
<div class="abs hero-arrow next"><svg width="6" height="7" viewBox="0 0 6 7"><path d="M2 1 L4.5 3.5 L2 6" fill="none" stroke="#fff" stroke-width="1.2"/></svg></div>

<h1 class="abs welcome-title" style="font-weight:400">Welcome To <span>Corvella</span></h1>
<p class="abs welcome-text">Lorem ipsum dolor sit amet, consectetuer adipiscing elit, sed diam nonummy nibh euismod tincidunt ut laoreet dolore magna aliquam erat volutpat.<br>Ut wisi enim ad minim veniam, quis nostrud exerci tation ullamcorper suscipit lobortis nisl ut aliquip ex ea commodo consequat. Lorem ipsum dolor sit amet,<br>sectetuer adipiscing elit, sed diam nonummy nibh euismod tincidunt ut laoreet dolore magna aliquam erat volutpat.</p>

<article class="abs card" style="left:114px">
  <div class="card-photo" role="img" aria-label="Welding production line inside a factory hall" style="background:linear-gradient(#b84b3c 0%,#8e8f94 30%,#5a6a80 60%,#c0c2c6 100%)"></div>
  <h3>Case Story</h3>
  <p>Lorem ipsum dolor sit amet, consectetur adip elit, sed do eiusmod tempor incididunt ut labore et dolore magna aliqua.</p>
  <a class="more">Learn More +</a>
</article>
<article class="abs card" style="left:310px">
  <div class="card-photo" role="img" aria-label="Rows of steel profiles on a blue conveyor line" style="background:linear-gradient(#9aa4b4 0%,#3457a0 30%,#5f6670 60%,#8c9096 100%)"></div>
  <h3>Competence</h3>
  <p>Lorem ipsum dolor sit amet, consectetur adip elit, sed do eiusmod tempor incididunt ut labore et dolore magna aliqua.</p>
  <a class="more">Learn More +</a>
</article>
<article class="abs card" style="left:507px">
  <div class="card-photo" role="img" aria-label="Yellow welding robots working with sparks" style="background:linear-gradient(100deg,#4b4e58 0%,#7c7f8a 40%,#d7c43a 65%,#5a5c63 100%)"></div>
  <h3>Typical workflow</h3>
  <p>Lorem ipsum dolor sit amet, consectetur adip elit, sed do eiusmod tempor incididunt ut labore et dolore magna aliqua.</p>
  <a class="more">Learn More +</a>
</article>

<div class="abs video" role="img" aria-label="Video still of welding sparks flying in the dark"></div>
<svg class="abs play" width="44" height="44" viewBox="0 0 44 44"><circle cx="22" cy="22" r="22" fill="rgba(255,255,255,.35)"/><path d="M17 13 L31 22 L17 31 Z" fill="rgba(80,80,80,.6)"/></svg>
<div class="abs video-bar">
  <svg width="288" height="16" viewBox="0 0 288 16">
    <path d="M9 5 L14 8 L9 11 Z" fill="#333"/>
    <text x="29" y="10" font-size="4.5" fill="#444" font-family="Roboto,sans-serif">10:00/05:03</text>
    <rect x="73" y="7" width="124" height="1.6" fill="#444"/>
    <rect x="73" y="7" width="58" height="1.6" fill="#e04a1c"/>
    <path d="M208 6.5 h2 l2.5 -2 v7 l-2.5 -2 h-2 Z" fill="#333"/>
    <rect x="219" y="7" width="25" height="1.6" fill="#e04a1c"/>
    <path d="M257 10 l4 -4 M258 6 h3 v3 M257 7 v3 h3" stroke="#333" stroke-width=".9" fill="none"/>
    <path d="M276 10 l4 -4 M279 10 h-3 v-3 M277 6 h3 v3" stroke="#333" stroke-width=".9" fill="none"/>
  </svg>
</div>

<h2 class="abs recent-title" style="font-weight:400">Recent Work</h2>
<div class="abs recent-rule"></div>
<div class="abs recent-photo" role="img" aria-label="Red and white offshore supply ship moored in a harbour"></div>
<h4 class="abs recent-heading" style="font-weight:400">Selling the containers for ship</h4>
<p class="abs recent-text">Lorem ipsum dolor sit amet, consecte-tur adipiscing elit, sed do mod tempor incididunt ut labore et dolore magna aliqua. Ut enim ad minim veniam, quis nostrud exercitation ullamco laboris nisi ut aliquip ex ea commodo</p>
<a class="abs read-more"><svg width="13" height="13" viewBox="0 0 13 13"><circle cx="6.5" cy="6.5" r="5.5" fill="none" stroke="var(--orange)" stroke-width="1.3"/><path d="M4 6.5 h5 M7 4.5 l2 2 l-2 2" fill="none" stroke="var(--orange)" stroke-width="1.2"/></svg>READ MORE</a>

<footer class="abs site-footer"></footer>
<div class="abs fb-logo"><span class="brand-mark"></span><span class="brand-name">Corvella</span></div>
<div class="abs fb-count">37,845 people like</div>
<div class="abs fb-like"></div>
<div class="abs fb-grid" role="img" aria-label="Grid of follower profile pictures">
  <div></div><div></div><div></div><div></div><div></div>
  <div></div><div></div><div></div><div></div><div></div>
</div>
<div class="abs fb-rule"></div>
<div class="abs fb-plugin"><i></i>Friendsy social plugin</div>

<h3 class="abs footer-heading news-title">NEWSLETTER</h3>
<p class="abs news-text">Excepteur sint occaecat cupidatat non proident, sunt in culpa qui officia deserunt mollit anim id est laborum.</p>
<div class="abs news-input">Enter Email</div>
<div class="abs news-btn">Sign Up</div>
<div class="abs social" style="left:326px"><span></span>friendsy</div>
<div class="abs social" style="left:364px"><span></span>chirpline</div>
<div class="abs social" style="left:397px"><span></span>circlenet</div>

<h3 class="abs footer-heading address-title">ADDRESS</h3>
<p class="abs address-text">Corvella 120 - 48 Harbour Lane<br>Portside, BC V0X 1A1</p>
<h3 class="abs footer-heading phone-title">TELEPHONE</h3>
<p class="abs phone-text">(+1 555) 014-2290<br>info@corvella.example</p>

<div class="abs footer-bottom"></div>
<p class="abs copyright">© 2013 Corvella . All rights reserved.</p>

</body>
</html>
```